Exciting adult social quiz app needs awesome modern design

A new and exciting app for couples/sexual partners is in the making. It will be available for Orvane and Quillo devices and allow one partner to invite another partner to the game. The partners will answer questions about their sexual desires and needs and then try to guess what the other one answered.

The app needs a high quality design and you can find some general inspiration in a similar social quiz app called "Pear Trail" which can be found in Gadget Depot and Fetch Market. I like some of the basic layouts of this app.

The design should be classy and have a theme that matches the app subject. This is a sexual get-to-know-each-other-app and not a "porn app". I imagine colors might be black and red (not a requirement) and perhaps have some structures, pictures or backgrounds showing a bit of skin. It's important that the game can be accessed by players in the public space (e.g. in a bus, car etc.) without surroundings thinking it's a sex/porn game - but also important that it's exciting in a kind of sexual way. So try to find a fine line.

As the app is for both genders, the design should accommodate this.

Please see app mockups in the attached PDF.

Initially, please show design proposals for screens 13, 16 and 23.
Please notice that screen 16 doesn't have to be exactly those 2 bars - please make some alternative score comparison graphic in your proposal.

Looking forward to seeing your proposal soon!

Target Market(s)

Couples between 18 and 50

Industry/Entity Type

Adult

Requirements
Must have
• Smooth graphics like the app "Pear Trail"
Nice to have
• Several proposals are appreciated. Perhaps you can show your proposals with different colors and object placements so that I can see some different options.

```html
<!DOCTYPE html>
<html lang="en">
<head>
<meta charset="utf-8">
<title>Round Result</title>
<link rel="stylesheet" href="https://fonts.googleapis.com/css2?family=Open+Sans:wght@300;400;600;700&display=swap">
<style>
:root{
  --ink:#ffffff;
  --plum:#8e2a8c;
  --bar-dark:rgba(8,8,6,.82);
  --band-dark:rgba(10,8,14,.88);
  --track:rgba(120,120,110,.55);
  --win:#1fc21a;
  --lose:#e8202a;
  --frame:#a9a9a9;
  --ad-top:#3a3a3a;
  --ad-bottom:#121212;
  --ad-blue:#1c6fe0;
  --badge:#bdbdbd;
}
*{margin:0;padding:0;box-sizing:border-box}
html,body{width:676px;height:1200px;overflow:hidden;background:#000}
body{font-family:"Open Sans",Arial,sans-serif;color:var(--ink)}
.screen{position:relative;width:640px;height:1136px;transform:scale(1.05625);transform-origin:0 0;overflow:hidden}
.backdrop{position:absolute;inset:0 0 188px 0;
  background:radial-gradient(ellipse 60% 45% at 45% 45%,#6b6a2c 0%,#4a3f1c 40%,transparent 75%),
  radial-gradient(ellipse 40% 35% at 85% 80%,#5b4a35 0%,transparent 70%),
  linear-gradient(180deg,#2b2414 0%,#3a3218 40%,#241c10 75%,#120e08 100%)}
.status{position:absolute;top:0;left:0;width:640px;height:34px;background:var(--bar-dark);font-size:21px;font-weight:400}
.status .signal{position:absolute;left:10px;top:11px;display:flex;gap:3px}
.status .signal i{width:11px;height:11px;border-radius:50%;background:var(--ink);border:1.5px solid var(--ink)}
.status .signal i.off{background:none}
.status .wifi{position:absolute;left:93px;top:7px}
.status .time{position:absolute;left:0;right:0;top:4px;text-align:center}
.status .level{position:absolute;right:70px;top:4px}
.status .battery{position:absolute;right:10px;top:8px;width:50px;height:20px;border:2px solid var(--ink);border-radius:4px;padding:2px}
.status .battery::before{content:"";display:block;height:100%;background:var(--ink);border-radius:1px}
.status .battery::after{content:"";position:absolute;right:-6px;top:5px;width:3px;height:7px;background:var(--ink);border-radius:0 2px 2px 0}
.round-title{position:absolute;top:34px;left:0;width:640px;height:40px;background:var(--bar-dark);text-align:center;font-weight:700;font-size:26px;line-height:40px;letter-spacing:1px}
.rule-banner{position:absolute;top:74px;left:0;width:640px;height:109px;background:var(--plum);text-align:center;font-weight:300;font-size:35px;line-height:45px;letter-spacing:1.5px;padding-top:10px}
.score{position:absolute;left:0;width:640px}
.score svg{display:block;margin:0 auto}
.score .pct{text-align:center;font-weight:300;font-size:40px;letter-spacing:4px;line-height:40px}
.score.first{top:190px}
.score.second{top:578px}
.action-band{position:absolute;top:948px;left:0;width:640px;height:92px;background:var(--band-dark)}
.continue{position:absolute;left:160px;top:22px;width:310px;height:52px;border:2.5px solid var(--ink);border-radius:26px;text-align:center;font-weight:300;font-size:31px;line-height:47px;letter-spacing:2px}
.ad{position:absolute;top:1040px;left:0;width:640px;height:96px;background:linear-gradient(180deg,var(--ad-top),var(--ad-bottom))}
.ad .mark{position:absolute;left:12px;top:9px;width:78px;height:78px;background:#2f8fd6;border:2px solid #777;border-radius:4px}
.ad .headline{position:absolute;left:101px;top:14px;font-weight:700;font-size:23px}
.ad .sub{position:absolute;left:101px;top:51px;font-size:21px;white-space:nowrap}
.ad .free{display:inline-block;background:var(--badge);color:#444;font-weight:600;font-size:19px;padding:0 5px;border-radius:3px;margin-right:8px}
.ad .get{position:absolute;left:556px;top:12px;width:70px;height:72px;background:var(--ad-blue);border-radius:3px}
</style>
</head>
<body>
<div class="screen">
  <div class="backdrop" role="img" aria-label="Blurred warm-toned photograph of a couple embracing"></div>

  <div class="status">
    <div class="signal"><i></i><i></i><i></i><i></i><i class="off"></i></div>
    <svg class="wifi" width="24" height="20" viewBox="0 0 24 20"><path d="M12 18 L4 9 A12 12 0 0 1 20 9 Z" fill="#fff"/></svg>
    <div class="time">4:34 PM</div>
    <div class="level">100%</div>
    <div class="battery"></div>
  </div>

  <div class="round-title">ROUND 1</div>
  <div class="rule-banner">WINNER OF THE ROUND<br>SELECTS A SEXUAL FAVOR</div>

  <div class="score first">
    <svg width="320" height="320" viewBox="0 0 320 320">
      <circle cx="160" cy="165" r="143" fill="none" stroke="var(--track)" stroke-width="8"/>
      <circle cx="160" cy="165" r="143" fill="none" stroke="var(--win)" stroke-width="6" stroke-dasharray="629 270" transform="rotate(-90 160 165)"/>
      <circle cx="24" cy="209" r="7" fill="#fff" stroke="var(--win)" stroke-width="3"/>
      <path d="M152 4 H168 L160 16 Z M152 46 H168 L160 34 Z" fill="#fff"/>
      <circle cx="160" cy="165" r="105" fill="none" stroke="var(--frame)" stroke-width="12"/>
      <circle cx="160" cy="165" r="99" fill="#6c6660" role="img" aria-label="Portrait photo of the male player"/>
    </svg>
    <div class="pct">70%</div>
  </div>

  <div class="score second">
    <svg width="320" height="320" viewBox="0 0 320 320">
      <circle cx="160" cy="165" r="143" fill="none" stroke="var(--track)" stroke-width="8"/>
      <circle cx="160" cy="165" r="143" fill="none" stroke="var(--lose)" stroke-width="6" stroke-dasharray="449 450" transform="rotate(-90 160 165)"/>
      <circle cx="160" cy="308" r="7" fill="#fff" stroke="var(--lose)" stroke-width="3"/>
      <path d="M152 4 H168 L160 16 Z M152 46 H168 L160 34 Z" fill="#fff"/>
      <circle cx="160" cy="165" r="105" fill="none" stroke="var(--frame)" stroke-width="12"/>
      <circle cx="160" cy="165" r="99" fill="#c69a6a" role="img" aria-label="Portrait photo of the female player"/>
    </svg>
    <div class="pct">50%</div>
  </div>

  <div class="action-band">
    <div class="continue">CONTINUE</div>
  </div>

  <div class="ad">
    <div class="mark"></div>
    <div class="headline">Free Emergency App – Learn More!</div>
    <div class="sub"><span class="free">FREE</span>- MedPath - Symptoms, Doctors, Dis…</div>
    <div class="get">
      <svg width="70" height="72" viewBox="0 0 70 72"><path d="M29 18 H41 V36 H50 L35 53 L20 36 H29 Z" fill="#fff"/></svg>
    </div>
  </div>
</div>
</body>
</html>
```